Fernwick

We require a professional design for a Cosmetic Surgery college. We have just submitted the request for our new logo which will be used on this card. We are the leaders in our field of education in Australia and this should be reflected in the quality of the card. People want to come and study with us because we are so outstanding in the field. Studying with us provides credibility, quality and courage.
Updates

Project Deadline Extended
Reason: Require updated logo to be used in design

Target Market(s)

25 - 40 year old professional women primarily from a medical background wanting to continue study in the cosmetic medical field, western speaking countries. The course average cost is 17k AU for 16 weeks.

Industry/Entity Type

Education

Requirements
Must have
• Must us the logo that is currently under design by this company.
Nice to have
• A medical twist very subtle would be nice possilbly rod of Asclepius.
Should not have
• Should not look old, we are dealing with modern medical concepts.
The logo that is being redesigned 3d silver, the attached logo is the old one.

```html
<!DOCTYPE html>
<html lang="en">
<head>
<meta charset="utf-8">
<title>Fernwick – Business Card</title>
<link href="https://fonts.googleapis.com/css2?family=Arimo:wght@400;700&display=swap" rel="stylesheet">
<style>
  :root {
    --backdrop: #2a2a2c;
    --teal: #13809f;
    --teal-deep: #0b6584;
    --teal-light: #2296b6;
    --paper: #ffffff;
    --stone: #a9abad;
    --stone-light: #bdbfc1;
    --ink: #3a3b3d;
    --silver: #d4d6d8;
  }
  * { margin: 0; padding: 0; box-sizing: border-box; }
  html, body {
    width: 1200px; height: 900px; overflow: hidden;
    background: var(--backdrop);
    font-family: "Arimo", Arial, sans-serif;
  }
  .canvas {
    position: relative; width: 1200px; height: 900px;
  }
  .card {
    position: absolute; left: 300px; width: 600px; height: 343px;
    overflow: hidden; box-shadow: 0 12px 30px rgba(0,0,0,.45);
  }
  .card--back { top: 80px; background: linear-gradient(135deg, var(--teal-light), var(--teal-deep)); }
  .card--front { top: 477px; background: var(--stone); }
  .card__shapes { position: absolute; inset: 0; }

  .wordmark { position: absolute; display: flex; align-items: center; gap: 12px; }
  .wordmark__dot { width: 46px; height: 46px; border-radius: 50%; }
  .wordmark__name { font-weight: 700; font-size: 34px; letter-spacing: 1px; line-height: 1; }
  .wordmark__tag { font-size: 9.5px; letter-spacing: 2px; margin-top: 4px; font-weight: 700; }

  .card--back .wordmark { left: 150px; top: 210px; }
  .card--back .wordmark__dot { background: var(--silver); }
  .card--back .wordmark__name, .card--back .wordmark__tag { color: var(--silver); }

  .card--front .wordmark { left: 38px; top: 82px; }
  .card--front .wordmark__dot { background: var(--teal); }
  .card--front .wordmark__name, .card--front .wordmark__tag { color: var(--teal); }

  .person { position: absolute; left: 40px; top: 228px; color: var(--ink); font-size: 13px; line-height: 1.35; }
  .person__name { color: var(--teal-deep); font-weight: 700; font-size: 22px; line-height: 1.1; }
  .person__role { margin-bottom: 10px; }
  .label { color: var(--teal-deep); font-weight: 700; margin-right: 4px; }
  .web { color: var(--teal-deep); font-weight: 700; }

  .office { position: absolute; left: 345px; top: 150px; color: var(--ink); font-size: 13px; line-height: 1.35; }
  .office__address { margin-bottom: 22px; }
</style>
</head>
<body>
<main class="canvas">

  <section class="card card--back" aria-label="Card back">
    <div class="wordmark">
      <span class="wordmark__dot"></span>
      <div>
        <div class="wordmark__name">FERNWICK</div>
        <div class="wordmark__tag">MEDICAL AESTHETICS EDUCATION</div>
      </div>
    </div>
  </section>

  <section class="card card--front" aria-label="Card front">
    <svg class="card__shapes" viewBox="0 0 600 343" preserveAspectRatio="none">
      <path d="M0 0 H600 V30 C500 110 380 180 0 218 Z" fill="var(--paper)"/>
      <path d="M600 8 C500 95 380 160 230 198 C390 175 500 120 600 62 Z" fill="var(--teal)"/>
    </svg>

    <div class="wordmark">
      <span class="wordmark__dot"></span>
      <div>
        <div class="wordmark__name">FERNWICK</div>
        <div class="wordmark__tag">MEDICAL AESTHETICS EDUCATION</div>
      </div>
    </div>

    <div class="person">
      <div class="person__name">Mira Dalton</div>
      <div class="person__role">Assistance</div>
      <div><span class="label">M</span>0400 000 000</div>
      <div><span class="label">E</span>mdalton@fernwick.com.au</div>
      <div class="web">www.fernwick.com.au</div>
    </div>

    <div class="office">
      <div class="office__address">Level 2, Nine Harbour Lane<br>Eastbrook Qld 4300</div>
      <div><span class="label">P</span>0755 000 123</div>
      <div><span class="label">F</span>0755 000 124</div>
      <div><span class="label">E</span>info@fernwick.com.au</div>
    </div>
  </section>

</main>
</body>
</html>
```